Brambly Crisps Label Design [Snack Brand]

We need an updated version of our label. It can either be a new concept or a refreshed take on our existing label. The new label needs to feel more modern. We need an execution in black and white and one in color.

There is a full creative brief attached that we hope will provide plenty of context and inspiration for the project.

Target Market(s)

Millennials and Gen Z: This is likely the most promising demo at the start. It plays well with the brand origin story and students love it. It is where initial word of mouth is likely to originate. Additionally, this demo is considered more adventurous with food choices and enjoy trying new flavors and creative combinations. Foodies and culinary enthusiasts Gift-givers Families

Industry/Entity Type

Food and Snacks

Requirements
Must have
• Any images containing examples of food should contain corn puffs (not popcorn)
Should not have

```html
<!DOCTYPE html>
<html lang="en">
<head>
<meta charset="utf-8">
<title>Brambly Crisps – Cheddar Caramel Corn Puffs Label</title>
<link href="https://fonts.googleapis.com/css2?family=Federo&family=Righteous&family=Montserrat:wght@400;500&display=swap" rel="stylesheet">
<style>
  :root {
    --page-bg: #ffffff;
    --kraft: #c4ab87;
    --ink: #141210;
    --ink-soft: #2a2520;
  }
  * { margin: 0; padding: 0; box-sizing: border-box; }
  html, body {
    width: 1200px;
    height: 1200px;
    overflow: hidden;
    background: var(--page-bg);
  }
  .canvas {
    position: relative;
    width: 1200px;
    height: 1200px;
  }
  .label {
    position: absolute;
    left: 168px;
    top: 60px;
    width: 864px;
    height: 1080px;
    background: var(--kraft);
  }
  .label-frame {
    position: absolute;
    inset: 20px;
    border: 2px solid var(--ink);
  }
  .brand-mark {
    position: absolute;
    left: 50%;
    top: 62px;
    width: 240px;
    height: 240px;
    margin-left: -120px;
    border-radius: 50%;
    background: var(--ink);
  }
  .brand-name {
    position: absolute;
    left: 0;
    right: 0;
    top: 336px;
    text-align: center;
    font-family: "Federo", sans-serif;
    font-weight: 400;
    font-size: 94px;
    letter-spacing: 1px;
    color: var(--ink);
    line-height: 1;
  }
  .product-flavor,
  .product-type {
    position: absolute;
    left: 0;
    right: 0;
    text-align: center;
    font-family: "Righteous", sans-serif;
    color: var(--ink);
    line-height: 1;
  }
  .product-flavor {
    top: 712px;
    font-size: 58px;
    letter-spacing: 1px;
  }
  .product-type {
    top: 782px;
    font-size: 84px;
    letter-spacing: 1px;
  }
  .diet-claim {
    position: absolute;
    left: 0;
    right: 0;
    top: 898px;
    text-align: center;
    font-family: "Montserrat", sans-serif;
    font-weight: 400;
    font-size: 30px;
    letter-spacing: 1px;
    color: var(--ink-soft);
  }
  .label-footer {
    position: absolute;
    left: 70px;
    right: 70px;
    top: 980px;
    display: flex;
    justify-content: space-between;
    font-family: "Montserrat", sans-serif;
    font-weight: 500;
    font-size: 28px;
    color: var(--ink);
  }
</style>
</head>
<body>
  <main class="canvas">
    <section class="label">
      <div class="label-frame"></div>
      <div class="brand-mark" role="img" aria-label="Brand emblem area"></div>
      <h1 class="brand-name">BRAMBLY CRISPS</h1>
      <p class="product-flavor">CHEDDAR CARAMEL</p>
      <p class="product-type">CORN PUFFS</p>
      <p class="diet-claim">GLUTEN FREE</p>
      <footer class="label-footer">
        <span class="website">bramblycrisps.com</span>
        <span class="net-weight">Net Wt. 7 oz (198.5 g)</span>
      </footer>
    </section>
  </main>
</body>
</html>
```